Label design for one hand cream.

The name of the company is Olvu. We are launching a hand cream that is also an immediate cleaner without any water. It removes dirt from your hands without using water. After the use, your hands will be soft. It could be used in your feet too.

The company logo reminds of plants, nature and we would like this approach too. Please, remove the words "Produtos Naturais" from the logo.

Reason: Not enough designs. Bad ones

Reason: I have not received one design that pleased us.

Target Market(s)

Public in General. Mostly women.

Industry/Entity Type

Cosmetics

Font styles to use
Sans Serif

Colors
33b8a4
00a990
9bcb3c
acd036
fee087
fece3e
ffc214
fbed22
fbee3e

Requirements
Must have
• You must use the words in the label. Please, see the file attached but just use the WORDS, not the same structure. The image must be 15,5cm high and 7,5 cm wide.
• Use a darker green and some GOLDEN lines or details. You can even put the Logo plant on the golden color.
• "Velmire Plus"
• "Ação 3 em 1: Esfoliante, limpeza e hidratação"
• "Regeneração Celular"
• "Calm Veil"
• Logo of the company "Olvu" (attached).
• Please, REMOVE the words "Produtos Naturais" from the logo.
• Elegance and show softness.
• Something that reminds of nature or fresh.
Should not have
• Strong colors or many images that distract the information.

```html
<!DOCTYPE html>
<html lang="pt">
<head>
<meta charset="utf-8">
<title>Olvu – Velmire Plus label</title>
<link rel="stylesheet" href="https://fonts.googleapis.com/css2?family=Open+Sans:wght@300;400;600;700&family=Roboto+Condensed:wght@700&display=swap">
<style>
  :root {
    --green-dark: #3f8a3a;
    --green-band: #5fa845;
    --green-brand: #6fb747;
    --green-stripe: #8fc76a;
    --green-field-top: #d3e9b2;
    --green-field-bottom: #e7f2d0;
    --green-leaf-a: #9fd07c;
    --green-leaf-b: #6fb04a;
    --gold: #d9ad2e;
    --white: #ffffff;
    --grey-text: #666666;
    --page-bg: #eeeeea;
  }
  * { margin: 0; padding: 0; box-sizing: border-box; }
  html, body { width: 1200px; height: 897px; overflow: hidden; background: var(--page-bg); }
  .label {
    position: absolute; left: 382px; top: 0;
    width: 436px; height: 897px;
    background: var(--white);
    overflow: hidden;
    font-family: "Open Sans", sans-serif;
  }
  .top-band {
    position: absolute; left: 0; top: 0; width: 100%; height: 53px;
    background: var(--green-band);
    color: var(--white);
    font-family: "Roboto Condensed", sans-serif; font-weight: 700;
    font-size: 18px; text-align: center; line-height: 76px;
  }
  .gold-line {
    position: absolute; left: 0; width: 100%; height: 2px;
    background: var(--gold);
  }
  .gold-line.under-band { top: 53px; }
  .brand {
    position: absolute; left: 0; top: 55px; width: 100%; height: 137px;
    display: flex; align-items: center; justify-content: center; gap: 14px;
  }
  .brand-dot { width: 30px; height: 30px; border-radius: 50%; background: var(--gold); }
  .brand-name {
    font-weight: 600; font-size: 84px; line-height: 1; color: var(--green-brand);
    letter-spacing: 1px;
  }
  .brand-rule {
    position: absolute; left: 0; top: 192px; width: 100%; height: 6px;
    background: var(--green-stripe);
  }
  .field {
    position: absolute; left: 0; top: 198px; width: 100%; height: 699px;
    background: linear-gradient(160deg, var(--green-field-top), var(--green-field-bottom));
  }
  .name-stripe {
    position: absolute; left: 30px; top: 198px; width: 90px; height: 699px;
    background: var(--green-stripe);
  }
  .vertical {
    position: absolute; white-space: nowrap;
    transform: rotate(-90deg); transform-origin: left top;
  }
  .product-name {
    left: 32px; top: 834px;
    font-size: 70px; line-height: 86px; font-weight: 600;
    color: var(--white); letter-spacing: 10px;
  }
  .product-tagline {
    left: 124px; top: 746px;
    font-size: 26px; line-height: 32px; font-weight: 300;
    color: var(--grey-text); letter-spacing: 2.6px;
  }
  .leaf-art {
    position: absolute; left: 172px; top: 344px; width: 244px; height: 416px;
    background: radial-gradient(ellipse at 60% 55%, var(--green-leaf-b), var(--green-leaf-a) 55%, rgba(159,208,124,0) 80%);
  }
  .benefits {
    position: absolute; left: 120px; top: 760px; width: 316px; height: 72px;
    background: var(--white);
    border-top: 2px solid var(--gold);
    border-bottom: 2px solid var(--gold);
    padding: 4px 0 0 28px;
    font-family: "Roboto Condensed", sans-serif; font-weight: 700;
    font-size: 25px; line-height: 31px; color: var(--grey-text);
  }
  .action-line {
    position: absolute; left: 134px; top: 846px; width: 292px;
    font-size: 13px; line-height: 18px; font-weight: 600;
    color: var(--green-dark);
  }
</style>
</head>
<body>
  <main class="label">
    <header class="top-band">Calm Veil</header>
    <div class="gold-line under-band"></div>
    <div class="brand">
      <span class="brand-dot"></span>
      <span class="brand-name">Olvu</span>
    </div>
    <div class="brand-rule"></div>
    <section class="field"></section>
    <div class="name-stripe"></div>
    <h1 class="vertical product-name">VELMIRE PLUS</h1>
    <p class="vertical product-tagline">Limpeza profunda para mãos e pés</p>
    <div class="leaf-art" role="img" aria-label="Large stylised pair of green leaves"></div>
    <div class="benefits">
      <p>Hidratante</p>
      <p>Regeneração Celular</p>
    </div>
    <p class="action-line">Ação 3 em 1: Esfoliante, limpeza e hidratação</p>
  </main>
</body>
</html>
```